Event Space Website (clone)

the name of the company is KINDLYHOST.com
i’ll have a logo shortly

i basically need a clone of the following website
https://ashlarrooms.example/
i would really like the design to be with stock photos
and then after choosing the winner i will supply my photos
(im doing some all new photo shoots this week)

id love the designer to put their OWN spin on this site

Target Market(s)

nyc urban market

Industry/Entity Type

Event Planning

Coding

Coded - Design and coding required

Number of Pages Required

1 page

Font styles to use
Serif

Requirements
Must have
• from top to bottom ill just list what i need copied

LOCATIONS FAQ CONTACT AND SOCIAL MEDIA LINKS NEED

i need the slider ... for sure

please change classics to current locations
please show
Harlem
Brooklyn
Bronx (for bronx show an image of coming soon)

please change events with a view to
Harlem Venues
1. Kindly Ashgrove
2. Kindly Upper Ashgrove

please change Our biggest and boldest to Brooklyn Venues
1. Kindly Fernwick
2. Kindly Holloway (1)
3. Kindly holloway (2)
4. Kindly Holloway rooftop

remove latest ventures
remove asian couple kissing

keep interested in this location
keep why chose us

keep contact us area
keep social media plug in
Nice to have
• ur own flair and style

PLEASE dont forget that all the individual sections
example
kindly ashgrove
kindly upper ashgrove
will have their own individual micro pages .... that will be placed under brooklyn venues (ive attached an example for clarity)

```html
<!DOCTYPE html>
<html lang="en">
<head>
<meta charset="utf-8">
<title>KINDLYHOST.com — Brooklyn &amp; Harlem Event Venues</title>
<link href="https://fonts.googleapis.com/css2?family=Libre+Baskerville:wght@400;700&family=Montserrat:wght@400;500;600;700&display=swap" rel="stylesheet">
<style>
:root{
  --ink:#0b0b0b;
  --white:#ffffff;
  --mist:#f4f5f8;
  --line:#d9dbe0;
  --muted:#5a5a5a;
  --icon-bg:#eceef2;
  --serif:"Libre Baskerville", Georgia, serif;
  --sans:"Montserrat", Arial, sans-serif;
}
*{box-sizing:border-box;margin:0;padding:0}
html,body{width:1200px;height:3995px;overflow:hidden}
body{position:relative;background:var(--white);color:var(--ink);font-family:var(--sans)}
.abs{position:absolute}
.center-text{text-align:center}

/* Hero */
.hero{left:0;top:0;width:1200px;height:597px;background:var(--ink);overflow:hidden}
.hero-strip{position:absolute;top:0;height:597px}
.strip-concert{left:0;width:225px;background:linear-gradient(180deg,#3a4a5c 0%,#2a2a2e 45%,#171717 100%)}
.strip-conference{left:237px;width:239px;background:linear-gradient(180deg,#6b4c2c 0%,#3a3026 50%,#1c1a1a 100%)}
.strip-decor{left:488px;width:233px;background:linear-gradient(180deg,#3b1f4f 0%,#6b3a8e 50%,#2f1840 100%)}
.strip-wedding{left:732px;width:232px;background:linear-gradient(180deg,#3d3832 0%,#6e655a 55%,#2e2a26 100%)}
.strip-banquet{left:975px;width:225px;background:linear-gradient(180deg,#4a3f33 0%,#6f6558 55%,#3a342d 100%)}
.hero-shade{position:absolute;left:0;top:0;width:1200px;height:140px;background:linear-gradient(180deg,rgba(0,0,0,.75),rgba(0,0,0,0))}
.brand{left:148px;top:18px;width:160px;text-align:center;color:var(--white)}
.brand-mark{display:block;width:38px;height:38px;margin:0 auto 8px;border:2px solid var(--white);border-radius:50%}
.brand-name{font-family:var(--serif);font-size:13px;letter-spacing:1px;white-space:nowrap}
.nav{top:40px;font-family:var(--sans);font-weight:600;font-size:13px;color:var(--white);letter-spacing:.5px;white-space:nowrap}
.nav-divider{left:959px;top:30px;width:1px;height:40px;background:rgba(255,255,255,.55)}
.social-dot{width:13px;height:13px;border-radius:50%;background:var(--white)}
.hero-title{left:0;top:260px;width:1200px;font-family:var(--serif);font-weight:700;font-size:45px;color:var(--white);letter-spacing:1px}
.hero-sub{left:0;top:320px;width:1200px;font-family:var(--sans);font-weight:600;font-size:22px;color:var(--white);letter-spacing:1.5px}

/* Section titles */
.section-title{left:0;width:1200px;font-family:var(--serif);font-weight:700;font-size:32px;letter-spacing:-.3px;white-space:nowrap}

/* Location cards */
.loc-card{top:753px;width:281px;height:281px;background:var(--white);box-shadow:0 4px 18px rgba(0,0,0,.07)}
.loc-photo{position:absolute;left:11px;top:2px;width:258px;height:208px;border-radius:10px}
.photo-harlem{background:linear-gradient(160deg,#6a6ea8 0%,#3a3f66 40%,#b7533a 75%,#2a2c40 100%)}
.photo-brooklyn{background:linear-gradient(160deg,#7f9a6a 0%,#405a44 45%,#7c8a8e 100%)}
.photo-soon{background:linear-gradient(160deg,#f6f7f9,#e6e8ec);display:flex;align-items:center;justify-content:center}
.soon-text{font-family:var(--sans);font-size:27px;letter-spacing:2px;color:#d4d6db;transform:rotate(-22deg);white-space:nowrap}
.loc-label{position:absolute;left:0;top:230px;width:100%;text-align:center;font-family:var(--serif);font-size:19px;color:#333}

/* Harlem venues */
.mist-band{left:0;top:1113px;width:915px;height:285px;background:var(--mist)}
.venue-wide{top:1256px;width:389px;height:294px}
.photo-hall{background:linear-gradient(170deg,#3a2410 0%,#8a5622 40%,#c98a3c 70%,#6a3e18 100%)}
.photo-gym{background:linear-gradient(180deg,#8e97a3 0%,#c9cdd1 45%,#b07a48 80%,#8c5c34 100%)}
.venue-tab{top:1496px;height:54px;background:var(--white);font-family:var(--serif);font-size:18px;color:#222;display:flex;align-items:center;padding:0 24px;white-space:nowrap}

/* Brooklyn venues */
.venue-tile{width:425px;height:288px;border-radius:3px;overflow:hidden}
.tile-frame{position:absolute;left:8px;top:8px;right:8px;bottom:8px;border:1.5px solid rgba(255,255,255,.85)}
.tile-fade{position:absolute;left:0;bottom:0;width:100%;height:120px;background:linear-gradient(180deg,rgba(0,0,0,0),rgba(0,0,0,.55))}
.tile-label{position:absolute;left:0;bottom:24px;width:100%;text-align:center;font-family:var(--serif);font-size:19px;color:var(--white);white-space:nowrap}
.photo-meeting{background:linear-gradient(180deg,#e8ebee 0%,#cfd3d6 50%,#6e6a66 100%)}
.photo-auditorium{background:linear-gradient(180deg,#9a9c9f 0%,#55585c 50%,#2c2f34 100%)}
.photo-gallery{background:linear-gradient(180deg,#d8dde2 0%,#f2f2f0 45%,#8a857e 100%)}
.photo-atrium{background:linear-gradient(180deg,#e4e8ec 0%,#c9d0c4 45%,#6c6a5a 100%)}

/* Interested */
.step{top:2436px;width:210px;text-align:center}
.step-icon{width:90px;height:90px;margin:0 auto;border-radius:50%;background:var(--ink);display:flex;align-items:center;justify-content:center}
.step-title{margin-top:18px;font-family:var(--serif);font-size:16px;color:#222;white-space:nowrap}
.step-copy{margin-top:8px;font-family:var(--sans);font-size:12px;line-height:20px;color:#222}

/* Why choose us */
.why-band{left:0;top:2687px;width:1200px;height:502px;background:var(--mist)}
.why-card{width:281px;height:124px;background:var(--white);display:flex;align-items:center;padding-left:27px}
.why-icon{width:72px;height:72px;border-radius:50%;background:var(--icon-bg);display:flex;align-items:center;justify-content:center;flex:none}
.why-label{margin-left:18px;font-family:var(--sans);font-weight:600;font-size:18px;color:var(--ink);white-space:nowrap}

/* Contact */
.contact-card{left:203px;top:3271px;width:794px;height:442px;background:var(--white);border-radius:10px;box-shadow:0 4px 22px rgba(0,0,0,.09)}
.field{height:45px;border:1px solid var(--line);border-radius:4px;font-family:var(--sans);font-size:12px;color:#555;padding:0 17px;display:flex;align-items:center;justify-content:space-between}
.field-area{align-items:flex-start;padding-top:15px;height:101px}
.submit{left:532px;top:3618px;width:135px;height:36px;background:var(--ink);color:var(--white);font-family:var(--sans);font-weight:700;font-size:13px;display:flex;align-items:center;justify-content:center;letter-spacing:.5px}

/* Footer */
.footer{left:0;top:3790px;width:1200px;height:205px;background:var(--ink);color:var(--white)}
.footer-link{top:58px;font-family:var(--sans);font-weight:600;font-size:13px;letter-spacing:.5px}
.footer-copy{left:0;top:88px;width:1200px;text-align:center;font-size:12px}
.footer-social{top:128px;width:28px;height:28px;border-radius:50%;background:var(--white)}
</style>
</head>
<body>

<!-- Hero -->
<header class="abs hero">
  <div class="hero-strip strip-concert" role="img" aria-label="Concert crowd with raised hands under stage lights"></div>
  <div class="hero-strip strip-conference" role="img" aria-label="Speaker addressing a conference audience"></div>
  <div class="hero-strip strip-decor" role="img" aria-label="Purple lit table decor with candles and flowers"></div>
  <div class="hero-strip strip-wedding" role="img" aria-label="Couple dancing at a wedding reception"></div>
  <div class="hero-strip strip-banquet" role="img" aria-label="Rustic banquet hall set with tables and chairs"></div>
  <div class="hero-shade"></div>

  <div class="abs brand"><span class="brand-mark"></span><span class="brand-name">KINDLYHOST.com</span></div>
  <span class="abs nav" style="left:656px">LOCATIONS</span>
  <span class="abs nav" style="left:778px">FAQs</span>
  <span class="abs nav" style="left:856px">CONTACT</span>
  <span class="abs nav-divider"></span>
  <span class="abs social-dot" style="left:992px;top:42px" aria-label="Social profile"></span>
  <span class="abs social-dot" style="left:1025px;top:42px" aria-label="Social profile"></span>

  <h1 class="abs hero-title center-text">UNIQUE &amp; ADAPTABLE</h1>
  <p class="abs hero-sub center-text">FOR HOW YOU WANT YOUR EVENT TO LOOK</p>
</header>

<!-- Current locations -->
<h2 class="abs section-title center-text" style="top:678px">CURRENT LOCATIONS</h2>
<div class="abs loc-card" style="left:161px">
  <div class="loc-photo photo-harlem" role="img" aria-label="City skyline at dusk with light trails along the river"></div>
  <div class="loc-label">HARLEM</div>
</div>
<div class="abs loc-card" style="left:460px">
  <div class="loc-photo photo-brooklyn" role="img" aria-label="Tree lined street with a neighbourhood sign"></div>
  <div class="loc-label">BROOKLYN</div>
</div>
<div class="abs loc-card" style="left:758px">
  <div class="loc-photo photo-soon"><span class="soon-text">COMING SOON</span></div>
  <div class="loc-label">BRONX</div>
</div>

<!-- Harlem venues -->
<div class="abs mist-band"></div>
<h2 class="abs section-title center-text" style="top:1185px">HARLEM VENUES</h2>
<div class="abs venue-wide photo-hall" style="left:161px" role="img" aria-label="Ballroom with chandelier and round banquet tables"></div>
<div class="abs venue-tab" style="left:327px;width:223px">KINDLY ASHGROVE</div>
<div class="abs venue-wide photo-gym" style="left:612px" role="img" aria-label="Open hall with wooden floor and tall windows"></div>
<div class="abs venue-tab" style="left:778px">KINDLY UPPER ASHGROVE</div>

<!-- Brooklyn venues -->
<h2 class="abs section-title center-text" style="top:1624px">BROOKLYN VENUES</h2>
<div class="abs venue-tile photo-meeting" style="left:161px;top:1693px" role="img" aria-label="Glass walled meeting room with projector screen">
  <div class="tile-fade"></div><div class="tile-frame"></div><div class="tile-label">KINDLY FERNWICK</div>
</div>
<div class="abs venue-tile photo-auditorium" style="left:612px;top:1693px" role="img" aria-label="Tiered auditorium facing a stage">
  <div class="tile-fade"></div><div class="tile-frame"></div><div class="tile-label">KINDLY HOLLOWAY 1</div>
</div>
<div class="abs venue-tile photo-gallery" style="left:161px;top:2000px" role="img" aria-label="Bright gallery space with pendant lamps and display walls">
  <div class="tile-fade"></div><div class="tile-frame"></div><div class="tile-label">KINDLY HOLLOWAY 2</div>
</div>
<div class="abs venue-tile photo-atrium" style="left:612px;top:2000px" role="img" aria-label="Glass roofed atrium with palm trees">
  <div class="tile-fade"></div><div class="tile-frame"></div><div class="tile-label">KINDLY HOLLOWAY ROOFTOP</div>
</div>

<!-- Interested -->
<h2 class="abs section-title center-text" style="top:2365px">INTERESTED IN THIS LOCATION</h2>
<div class="abs step" style="left:157px">
  <div class="step-icon"><svg width="44" height="44" viewBox="0 0 44 44" fill="none" stroke="#fff" stroke-width="2"><rect x="6" y="8" width="32" height="28" rx="2"/><path d="M6 14h32"/><path d="M13 20l9 7 9-7"/><rect x="13" y="20" width="18" height="11"/></svg></div>
  <div class="step-title">Send Us A Note</div>
  <div class="step-copy">We Don't Keep You Waiting</div>
</div>
<div class="abs step" style="left:382px">
  <div class="step-icon"><svg width="44" height="44" viewBox="0 0 44 44" fill="none" stroke="#fff" stroke-width="2"><path d="M22 34s-10-10-10-17a10 10 0 0 1 20 0c0 7-10 17-10 17z"/><circle cx="22" cy="17" r="4"/><path d="M8 30l-2 8h32l-2-8"/></svg></div>
  <div class="step-title">Check Out The Location</div>
  <div class="step-copy">Take a guided tour with<br>a venue rep</div>
</div>
<div class="abs step" style="left:607px">
  <div class="step-icon"><svg width="44" height="44" viewBox="0 0 44 44" fill="none" stroke="#fff" stroke-width="2"><rect x="6" y="9" width="32" height="28" rx="2"/><path d="M6 16h32M14 5v8M30 5v8"/><circle cx="14" cy="23" r="2"/><circle cx="22" cy="23" r="2"/><circle cx="30" cy="23" r="2"/><circle cx="14" cy="30" r="2"/><circle cx="22" cy="30" r="2"/><circle cx="30" cy="30" r="2"/></svg></div>
  <div class="step-title">Pick Your Perfect Date</div>
  <div class="step-copy">We Can Help You Find<br>the Right Date</div>
</div>
<div class="abs step" style="left:831px">
  <div class="step-icon"><svg width="44" height="44" viewBox="0 0 44 44" fill="none" stroke="#fff" stroke-width="2"><rect x="9" y="6" width="26" height="32" rx="2"/><path d="M13 14l2 2 4-4M13 23l2 2 4-4M13 32l2 2 4-4M23 14h8M23 23h8M23 32h8"/></svg></div>
  <div class="step-title">Plan</div>
  <div class="step-copy">Check Out Our Vendors<br>Have Questions?</div>
</div>

<!-- Why choose us -->
<div class="abs why-band"></div>
<h2 class="abs section-title center-text" style="top:2757px">WHY CHOOSE US</h2>
<div class="abs why-card" style="left:161px;top:2831px">
  <div class="why-icon"><svg width="40" height="40" viewBox="0 0 40 40" fill="none" stroke="#222" stroke-width="1.8"><circle cx="20" cy="20" r="14"/><path d="M13 20l5 5 10-10"/></svg></div>
  <span class="why-label">Easy</span>
</div>
<div class="abs why-card" style="left:459px;top:2831px">
  <div class="why-icon"><svg width="40" height="40" viewBox="0 0 40 40" fill="none" stroke="#222" stroke-width="1.8"><rect x="8" y="6" width="14" height="26" rx="2"/><rect x="22" y="14" width="11" height="20" rx="2"/><path d="M12 12h6M12 17h6M25 20h5"/></svg></div>
  <span class="why-label">Responsive</span>
</div>
<div class="abs why-card" style="left:758px;top:2831px">
  <div class="why-icon"><svg width="40" height="40" viewBox="0 0 40 40" fill="none" stroke="#222" stroke-width="1.8"><path d="M20 32S7 24 7 15a6.5 6.5 0 0 1 13-2 6.5 6.5 0 0 1 13 2c0 9-13 17-13 17z"/></svg></div>
  <span class="why-label">Customizable</span>
</div>
<div class="abs why-card" style="left:310px;top:2988px">
  <div class="why-icon"><svg width="40" height="40" viewBox="0 0 40 40" fill="none" stroke="#222" stroke-width="1.8"><circle cx="14" cy="13" r="4"/><circle cx="27" cy="13" r="4"/><path d="M7 30v-5a7 7 0 0 1 14 0v5M20 30v-5a7 7 0 0 1 14 0v5M5 30h30"/></svg></div>
  <span class="why-label">Vendors</span>
</div>
<div class="abs why-card" style="left:609px;top:2988px">
  <div class="why-icon"><svg width="40" height="40" viewBox="0 0 40 40" fill="none" stroke="#222" stroke-width="1.8"><circle cx="17" cy="17" r="10"/><path d="M24 24l9 9"/><path d="M12 17h10M17 12v10"/></svg></div>
  <span class="why-label">Transparent</span>
</div>

<!-- Contact -->
<section class="abs contact-card" aria-label="Contact form"></section>
<h2 class="abs section-title center-text" style="top:3303px">CONTACT US</h2>
<div class="abs field" style="left:245px;top:3364px;width:229px">Your Name*</div>
<div class="abs field" style="left:485px;top:3364px;width:230px">Your Email*</div>
<div class="abs field" style="left:726px;top:3364px;width:229px">Your Phone*</div>
<div class="abs field" style="left:245px;top:3429px;width:347px">Type of Event*<svg width="10" height="6" viewBox="0 0 10 6" fill="none" stroke="#555" stroke-width="1.4"><path d="M1 1l4 4 4-4"/></svg></div>
<div class="abs field" style="left:605px;top:3429px;width:350px">Venue(s) of Interest*<svg width="10" height="6" viewBox="0 0 10 6" fill="none" stroke="#555" stroke-width="1.4"><path d="M1 1l4 4 4-4"/></svg></div>
<div class="abs field field-area" style="left:245px;top:3496px;width:710px">Message*</div>
<div class="abs submit">SUBMIT</div>

<!-- Footer -->
<footer class="abs footer">
  <span class="abs footer-link" style="left:444px">LOCATIONS</span>
  <span class="abs footer-link" style="left:587px">FAQs</span>
  <span class="abs footer-link" style="left:685px">CONTACT</span>
  <p class="abs footer-copy">Copyright © 2021 KINDLYHOST BROOKLYN HARLEM. All Rights Reserved.</p>
  <span class="abs footer-social" style="left:565px" aria-label="Social profile"></span>
  <span class="abs footer-social" style="left:606px" aria-label="Social profile"></span>
</footer>

</body>
</html>
```